Real estate development company, seeking investors and joint venture partners to fund

i have attached a investor proposal document to attact joint venture money partners to invest in property development. the existing document i have attached need s to be polised to a professional standard and needs to be in word , so i can edit the content on ongoing basis i.e. numbers and photos etc . this document will be updated with new opportunites, propoerties, feasibility edited and emailed to potential investors. This document needs to be Red hot!! Company name Bright meadow collective. All tables, place holders for photos need to be provided so i can easily remove and paste new /updated photos.

Target Market(s)

investors , money partners property developers

Requirements
Must have
• Design to be in word document

Content should be modifyable by me as each project will have unique cost, sales etc

i want to be able to email to my clients

i may also print as required
Nice to have
• Feel free to modify table/images/look and feel

```html
<!DOCTYPE html>
<html lang="en">
<head>
<meta charset="utf-8">
<title>Investor Report – Bright meadow collective</title>
<link rel="stylesheet" href="https://fonts.googleapis.com/css2?family=Cinzel:wght@400;600;700&family=Cormorant+Garamond:wght@400;500;600&family=Montserrat:wght@400;600&display=swap">
<style>
:root{
  --backdrop:#e89f5e;
  --orange:#e07c24;
  --ink:#1c1c1c;
  --charcoal:#2a2a2a;
  --paper:#ffffff;
  --rule:#8a8a8a;
  --muted:#3c3c3c;
  --serif-display:'Cinzel', serif;
  --serif-text:'Cormorant Garamond', serif;
  --sans:'Montserrat', sans-serif;
}
*{margin:0;padding:0;box-sizing:border-box}
html,body{width:1200px;height:2500px;overflow:hidden;background:var(--backdrop)}
.stage{position:absolute;left:0;top:0;width:1236px;height:2576px;transform:scale(0.9709);transform-origin:0 0}
.page{position:absolute;background:var(--paper);overflow:hidden}
.abs{position:absolute}
.photo{position:absolute}

/* cover */
.cover{left:365px;top:86px;width:511px;height:722px}
.cover .bar-orange{left:35px;top:41px;width:151px;height:12px;background:var(--orange)}
.cover .bar-black{left:186px;top:41px;width:214px;height:12px;background:var(--ink)}
.cover .brand{left:412px;top:35px;font:400 19px var(--serif-display);color:var(--orange);letter-spacing:.5px}
.cover .kicker{left:35px;top:73px;font:400 9.5px var(--sans);color:var(--muted)}
.cover .title-1{left:36px;top:80px;font:700 72px/1 var(--serif-display);color:var(--orange);letter-spacing:1px}
.cover .title-2{left:188px;top:160px;font:700 54px/1 var(--serif-display);color:var(--ink);letter-spacing:6px}
.cover .title-3{left:186px;top:213px;font:400 25px/1 var(--serif-text);color:var(--muted);letter-spacing:2.2px}
.cover .summary{left:186px;top:592px;width:290px;font:400 9.3px/1.25 var(--sans);color:var(--muted);text-align:justify}
.cover .prepared{left:186px;top:660px;font:400 9.5px var(--sans);color:var(--ink)}
.cover .prepared b{font-weight:600}
.cover .footer-rule{left:35px;top:687px;width:441px;height:1px;background:var(--rule)}
.cover .url{right:35px;top:694px;font:400 7px var(--serif-text);color:var(--orange)}

/* spreads */
.spread{position:absolute;left:107px;width:1021px;height:722px}
.spread-1{top:904px}
.spread-2{top:1728px}
.spread .page{top:0;height:722px;width:510px}
.spread .page.right{left:510px;width:511px;border-left:1px solid #ddd}
.spread .page.left{left:0}
.running-head{position:absolute;left:35px;top:15px;width:441px;height:19px;background:var(--orange);
  display:flex;justify-content:space-between;align-items:center;padding:0 6px;
  font:400 8.5px var(--serif-text);color:#4a2a10;letter-spacing:.4px}
.page.right .running-head{left:36px}
.page-rule{position:absolute;left:35px;top:686px;width:441px;height:1px;background:var(--rule)}
.page.right .page-rule{left:36px}
.folio{position:absolute;top:693px;font:400 7px var(--serif-text);color:var(--orange);letter-spacing:.3px}
.page.left .folio{left:35px}
.page.right .folio{right:35px}

.section-title{position:absolute;font:500 18px var(--serif-text);color:var(--ink);letter-spacing:1px}
.body-copy{position:absolute;font:400 9.3px/1.22 var(--sans);color:var(--muted);text-align:justify}
.body-copy p+p{margin-top:11px}

.intro-title{left:35px;top:58px}
.intro-copy{left:35px;top:99px;width:440px}
.intro-photo{left:35px;top:346px;width:440px;height:318px;
  background:linear-gradient(160deg,#e9e4dc 0%,#cdb89a 45%,#a67c4e 80%,#6d4a2a 100%)}

.toc-title{left:36px;top:62px;font-size:21px}
.toc{position:absolute;left:36px;top:112px;list-style:none}
.toc li{font:400 16.5px/41.3px var(--serif-text);color:var(--muted);letter-spacing:.6px}
.toc .sep{margin:0 8px}
.side-note{left:338px;top:62px;width:138px;height:457px;background:var(--charcoal);
  padding:16px 20px;font:400 9.3px/1.3 var(--serif-text);color:#e6e6e6;text-align:justify}
.side-block{left:338px;top:527px;width:138px;height:137px;background:var(--orange)}

.page-heading{position:absolute;left:0;width:100%;text-align:center;font:700 27px var(--serif-display);color:var(--ink);letter-spacing:2px}
.feature-frame{position:absolute;left:35px;top:94px;width:441px;height:268px;border-top:4px solid var(--charcoal);border-bottom:6px solid var(--orange)}
.page.right .feature-frame{left:36px}
.meeting-photo{background:linear-gradient(135deg,#20283a 0%,#4b5366 40%,#c9cbcf 65%,#e8e8e8 100%)}
.map-area{background:linear-gradient(160deg,#f3ead2 0%,#eadfbf 40%,#bfe0ea 60%,#9fd0e6 80%,#c9dfb4 100%)}

.facts{position:absolute;left:35px;top:372px;width:210px;font:400 9.3px/1.25 var(--sans);color:var(--muted)}
.facts h4{font:600 9.5px var(--sans);color:var(--ink);margin-bottom:12px}
.facts p{margin-bottom:12px}
.facts .outcome{margin-bottom:13px}
.facts .closing{margin-top:22px;margin-bottom:0}
.townhouse-photo{left:261px;top:373px;width:214px;height:297px;
  background:linear-gradient(180deg,#cfe2f3 0%,#e9eef3 30%,#b5826a 55%,#d9c3a8 80%,#a9b0a0 100%)}

.overview-title{position:absolute;left:36px;top:400px;font:400 21px var(--serif-text);color:var(--ink);letter-spacing:5px}
.overview-rule{position:absolute;left:187px;top:414px;width:289px;height:2px;background:var(--ink)}
.stats{position:absolute;left:36px;top:422px;width:136px;list-style:none}
.stats li{font:400 9px var(--sans);color:var(--muted);padding:4px 0 6px;border-bottom:1px solid var(--rule)}
.overview-copy{left:186px;top:423px;width:290px}
.overview-copy p+p{margin-top:9px}
.aerial-photo{left:36px;top:496px;width:140px;height:176px;
  background:linear-gradient(150deg,#5c7a4a 0%,#8a9a86 40%,#b8bcbf 60%,#6f8a5a 100%)}
</style>
</head>
<body>
<div class="stage">

  <!-- Cover -->
  <section class="page cover">
    <div class="abs bar-orange"></div>
    <div class="abs bar-black"></div>
    <div class="abs brand">BRIGHT MEADOW</div>
    <p class="abs kicker">Obisi untus sum faccabore num imusae plibus, aute nes verum aut fugita</p>
    <h1 class="abs title-1">INVESTOR</h1>
    <div class="abs title-2">REPORT</div>
    <div class="abs title-3">Dual OCC Development</div>
    <div class="photo" style="left:35px;top:169px;width:139px;height:501px;background:linear-gradient(90deg,#c21a1a 0%,#e0332a 60%,#dfe6ea 100%)" role="img" aria-label="Photo of a stack of red wooden blocks"></div>
    <div class="photo" style="left:186px;top:249px;width:290px;height:331px;background:linear-gradient(180deg,#f2f2f2 0%,#f2f2f2 22%,#6b6048 38%,#c79a45 48%,#f0f0f0 56%,#eeeeee 100%)" role="img" aria-label="Photo of a city skyline resting above an open hand"></div>
    <p class="abs summary">Ant qui aut rem. Taqui quia solum experro ipicidu ciuntur aut doluptatum quia volupta eperroviti bea simus, et rest, od maximoluptas et a sendant officae natestrum a sed molores apis dolorero beritam cusam, omnisqui iducillam rectureperum fugit aspient exerorempor as dit a doluptio corum remquis.</p>
    <p class="abs prepared">Prepared by: <b>Priya Ramanathan, BMC ABN</b></p>
    <div class="abs footer-rule"></div>
    <div class="abs url">www.brightmeadow.com</div>
  </section>

  <!-- Spread: introduction & contents -->
  <div class="spread spread-1">
    <section class="page left">
      <header class="running-head"><span>CREATIVITY</span><span>TRADING NAME</span></header>
      <h2 class="section-title intro-title">INTRODUCTION</h2>
      <div class="body-copy intro-copy">
        <p>Exped qui que perrum faceris miliquo magnat liciatur, temolor repudant lamentibus esequas et iunt.</p>
        <p>Bo. Ut eum quam corent ullatqui volore sam des dolor autet facestius dem dolor aci raeria que erum re, si in es eum exerum facid ma vereperit opta dolorestet rem quo earis aut reption pror solupta autem fugiatenis quodi cone dolorem nobitiorios veles delibea volorerum et apitisquam rerum lam, andam eumquis ciuscip icimini hicipsa ndunto molenduci nobit erum faceperias as sum re plabore pudam, occullo rescia parchit occuptae dolenis de non nonsedis ut ipid unt omnimin coritib erumquae. Itat quassim renis erchiciam in rerum ad maio estiis entis atent, si odis ulparum doluptate laut peditam, sam, se nullam qui dolorroris essitas et aboreped erio omnimuscia nus maiore pliquam voluptae cusam eatectur, te nitiuntus, idelent.</p>
        <p>At. Ehendus, tenihil ipis dipis ea duciis quo debita doluptis id es quas sum hit quo dolorio officiis dolupta es sum nam quati quidebis et facerrum re vidignihit raepuda ipitate endi ut veliquam etur audae doles sam volupta conet doluptas modis arciasp ereperum exces que nes de nus eum ipite comnia parum quideni mpossi offic tem faceperio experenditas aut latent faceria velit hicid quiberum cum, oditatu rehendellaut andicimo to everum hitam aut officti busaectia quia si quam aceatur sandipsant quos et is peremqui nescia accabor aut eum iduntus, simagnihilit laborem rem quam simus anis exceper epeliant eatemque nates eos ea nonsed molo doluptae di que velenessit is con perro ea cus.</p>
      </div>
      <div class="photo intro-photo" role="img" aria-label="Photo of a toy house under a magnifying glass above wooden blocks spelling invest"></div>
      <div class="page-rule"></div>
      <div class="folio">BRIGHT MEADOW COLLECTIVE</div>
    </section>

    <section class="page right">
      <header class="running-head"><span>Tel.: 0412-555-018 &nbsp;|&nbsp; E: info@brightmeadow.com.au</span><span>PROPOSAL</span></header>
      <h2 class="section-title toc-title">TABLE OF CONTENTS</h2>
      <ol class="toc">
        <li>PROPOSAL<span class="sep">|</span>4</li>
        <li>LOCATION<span class="sep">|</span>4</li>
        <li>PHOTOS<span class="sep">|</span>5</li>
        <li>FINANCIAL FEASIBILITY<span class="sep">|</span>5</li>
        <li>CASH FLOW ANALYSIS<span class="sep">|</span>6</li>
        <li>CAPITAL REQUIREMENTS<span class="sep">|</span>7</li>
        <li>SUBURB PROFILE<span class="sep">|</span>8</li>
        <li>COMPARABLE SALES DATA<span class="sep">|</span>10</li>
        <li>PLANNING INFORMATION<span class="sep">|</span>13</li>
        <li>TESTIMONIALS<span class="sep">|</span>16</li>
        <li>WHO ARE YOU?<span class="sep">|</span>16</li>
        <li>CONTACT<span class="sep">|</span>20</li>
      </ol>
      <aside class="abs side-note">Musam rehendus ut aut laudis rerepro ea volum conet vero el imaximagnati ut audae parum que lic tectempor aut omni num endebit pellit, si corit resti nonserro mos ese porita quo vellis voluptatur, conseque lab incte que voles re soluptus, cullic teniscid quideste dissent ectotatur sequisi musandu sapistrum volut eatemquunt, earcietur si dis con conserferia evene eum aspis res atur? Fereratemqui ut vendipi cipissint eaque essin reiunt posam, nim sernatem latiis maximodissi rem fugitatem il eum rerio cus acia nonsequia quassere et aut as doloreptio minvelibus, quam hari officturem rem veni tendis diaturia sinverumquos et es sintius eum faci cullescitium incius, sit il ipicae. Nequam corrum voluptas ellest, omniae. Et veriatinto beat</aside>
      <div class="abs side-block"></div>
      <div class="page-rule"></div>
      <div class="folio">BRIGHT MEADOW COLLECTIVE</div>
    </section>
  </div>

  <!-- Spread: proposal & location -->
  <div class="spread spread-2">
    <section class="page left">
      <header class="running-head"><span>CREATIVITY</span><span>TRADING NAME</span></header>
      <h2 class="page-heading" style="top:52px">PROPOSAL</h2>
      <div class="feature-frame meeting-photo" role="img" aria-label="Photo of business people reviewing documents at a laptop"></div>
      <div class="facts">
        <h4>Project Goal:</h4>
        <p>Purchase an existing house on a block of land, obtain development approval to demolish existing house and build two townhouses (dual occupancy side by side)</p>
        <h4>Project Outcomes:</h4>
        <p class="outcome">Project Type: 2 Townhouse Development</p>
        <p class="outcome">Total Project Costs: $1,900,000</p>
        <p class="outcome">Total Cash/Equity Required: $627,991</p>
        <p class="outcome">Indicative Project Net Profit: $250,093</p>
        <p class="outcome">Indicative Project Return: 40%</p>
        <p class="closing">Erum ut quatio dolesed ulpa conserunti ius, ullum sequidigeni ut adia dolum rem et eum des destore vent eaque nonsect emolorrorem et mi, oditatectat pariaes equiaspitae et quo et aut occum non nobis etur, ventiore omnistis voluptios repercima</p>
      </div>
      <div class="photo townhouse-photo" role="img" aria-label="Photo of a pair of two storey townhouses"></div>
      <div class="page-rule"></div>
      <div class="folio">4 &nbsp;BRIGHT MEADOW COLLECTIVE</div>
    </section>

    <section class="page right">
      <header class="running-head"><span>Tel.: 0412-555-018 &nbsp;|&nbsp; E: info@brightmeadow.com.au</span><span>PROPOSAL</span></header>
      <h2 class="page-heading" style="top:50px">PROJECT LOCATION</h2>
      <div class="feature-frame map-area" role="img" aria-label="Map of the city showing the project site and nearby suburbs"></div>
      <h3 class="overview-title">OVERVIEW</h3>
      <div class="overview-rule"></div>
      <ul class="stats">
        <li>Station : 1.4 KM</li>
        <li>Freeway Access: 1.5 KM</li>
        <li>Shopping Centre: 1 KM</li>
      </ul>
      <div class="body-copy overview-copy">
        <p>Nest, idusdae. Peratiate earum debitat faceati onsequis suntio. Et ullest a seque nonse conectet aut eos et laut et faciaesto evellam quissita ditae id quod qui quam solor ma dolum eat. Offici dollande omnit officim ostorepudia sae re lam, quatiuntur? Igendis re eatende rrorrovit rempe doluptae vero mintur? Quia etur sunt.</p>
        <p>Turibuscium de ped maiorio este dit magnatur siti dem eum, officto restior as eatqui asperum que nus que re cus essum dis moles accusdae. Et faciasped erferias ressum ut dolupta dolupta con natumenimi, sam fugitam arit qui ommo et et volorat assitaquiate sa culpa destrumet est, consequis ni a dem a quosam sequid quae plitatur, in peribus aut laborum landebit fugit qui diciis delicabore ideliquam, simus.</p>
        <p>Ehendi que ma quistiatur aut offictur? Occum, sunt incius.</p>
        <p>Nem as dolorpor adis et de sectissitat. Os eossit as remporit lab idemporis reiuntibus ne perfersperum ello occusapel invel id quasinv enihill atibus ditatur adis min consecum invero modis molorit asperibus, quia vellace pudigen ihillorem el magnam.</p>
      </div>
      <div class="photo aerial-photo" role="img" aria-label="Aerial photo of a freeway interchange"></div>
      <div class="page-rule"></div>
      <div class="folio">BRIGHT MEADOW COLLECTIVE 5</div>
    </section>
  </div>

</div>
</body>
</html>
```